Velmora Partners - website for real estate investment company

Create a bold, modern website that reflects Velmora’s success, professionalism, and credibility.
The design must stand out while maintaining a polished, corporate tone. (bold, but understated)
The client just created a new logo, and the website design must be in sync with the logo design. Information about the logo colors, fonts, and message are in the attached design brief.
Updates

Target Market(s)

b2b: banks, brokers, institutional partners, vendors, and property sellers.

Industry/Entity Type

real estate investment company

Number of Pages Required

1 page

Font styles to use
Sans Serif

Colors

Designer to choose colors to be used in the design.

Requirements
Must have
• 1. homepage design (psd) 2. a top banner image (psd) for a default inner page
Nice to have
• please see attached design brief
Should not have

```html
<!DOCTYPE html>
<html lang="en">
<head>
<meta charset="UTF-8">
<title>Velmora Partners</title>
<link href="https://fonts.googleapis.com/css2?family=Barlow:wght@300;400;500;600;700;800&display=swap" rel="stylesheet">
<style>
:root{
  --red:#e3222c;
  --ink:#1c1c1c;
  --dark:#141414;
  --dark-2:#1d1d1d;
  --grey:#6b6b6b;
  --light:#ececec;
  --white:#ffffff;
}
*{margin:0;padding:0;box-sizing:border-box}
html,body{width:1200px;height:3421px;overflow:hidden}
body{font-family:'Barlow',sans-serif;background:var(--white);position:relative;color:var(--ink)}
.abs{position:absolute}

/* hero */
.hero{position:absolute;left:0;top:0;width:1200px;height:682px;overflow:hidden;
  background:linear-gradient(180deg,#3d4660 0%,#4b4a55 30%,#5a4c46 55%,#2c2c30 100%)}
.hero-band{position:absolute;left:694px;top:0;width:372px;height:682px;background:rgba(255,255,255,.08)}
.brand{position:absolute;left:106px;top:26px;color:var(--white);font-weight:700;font-size:38px;letter-spacing:1px}
.nav{position:absolute;top:0;left:0;width:1200px;height:104px}
.nav-item{position:absolute;top:0;height:104px;display:flex;flex-direction:column;align-items:center;justify-content:flex-end;padding-bottom:12px;color:#d8d8d8;font-size:16px;transform:translateX(-50%);white-space:nowrap}
.nav-item svg{width:30px;height:30px;margin-bottom:12px;stroke:currentColor;fill:none;stroke-width:1.5}
.nav-item.active{background:var(--red);color:var(--white);font-weight:600;width:72px}
.hero h1{position:absolute;top:220px;left:0;width:1200px;text-align:center;color:var(--white);font-size:58px;font-weight:700;letter-spacing:.5px}
.hero p{position:absolute;top:303px;left:250px;width:700px;text-align:center;color:#eaeaea;font-size:20px;font-weight:300;line-height:30px}
.btn{position:absolute;border:2px solid var(--white);border-radius:30px;color:var(--white);font-weight:600;font-size:18px;display:flex;align-items:center;justify-content:center;letter-spacing:.5px}
.play{position:absolute;left:530px;top:588px}

/* stats section */
.shape{position:absolute;left:0;top:0}
.founded{position:absolute;top:770px;width:1200px;text-align:center;font-size:56px;font-weight:800;color:transparent;-webkit-text-stroke:2px var(--red);letter-spacing:2px}
.digit{position:absolute;top:818px;font-size:400px;font-weight:800;line-height:1;color:#7a746c;text-shadow:6px 6px 0 #222}
.stat-num{position:absolute;font-size:48px;font-weight:700;color:var(--red)}
.stat-text{position:absolute;font-size:32px;font-weight:400;line-height:40px;color:var(--ink)}

/* footer */
.footer{position:absolute;left:0;top:2520px;width:1200px;height:901px;background:var(--dark);overflow:hidden}
.foot-brand{position:absolute;top:60px;width:1200px;text-align:center;color:var(--grey);font-weight:800;font-size:120px;letter-spacing:2px;line-height:1}
.form-title{position:absolute;top:208px;width:1200px;text-align:center;color:var(--white);font-weight:600;font-size:18px;letter-spacing:.5px}
.field{position:absolute;left:248px;width:705px;border-bottom:1px solid #5a5a5a;text-align:center;color:#bcbcbc}
.field-label{font-size:13px;letter-spacing:.5px}
.field-value{font-size:32px;color:var(--white);font-weight:500}
.sep{position:absolute;left:0;top:663px;width:1200px;height:1px;background:#2c2c2c}
.contact-icon{position:absolute;width:96px;height:96px;border-radius:50%;background:var(--white);border:6px solid #c9c9c9}
.contact-icon svg{position:absolute;left:50%;top:50%;transform:translate(-50%,-50%)}
.contact-text{position:absolute;color:#c8c8c8;font-size:17px;line-height:28px;font-weight:500;white-space:nowrap}
.contact-text strong{color:var(--white);font-weight:600;font-size:18px}
.copy{position:absolute;top:856px;width:1200px;text-align:center;color:#bdbdbd;font-size:17px;font-weight:600}
.copy span{color:var(--red)}
</style>
</head>
<body>

<header class="hero">
  <div class="abs" style="inset:0" role="img" aria-label="City skyline at dusk seen from above"></div>
  <div class="hero-band"></div>
  <svg class="shape" width="1200" height="682"><polygon points="1066,0 1200,0 1200,70 1066,206" fill="#e3222c" opacity=".9"/></svg>
  <div class="brand">VELMORA</div>
  <nav class="nav">
    <div class="nav-item active" style="left:405px"><svg viewBox="0 0 30 30"><path d="M4 14 15 4l11 10M7 12v14h16V12M12 26v-7h6v7"/></svg>Home</div>
    <div class="nav-item" style="left:494px"><svg viewBox="0 0 30 30"><path d="M7 4h12l5 5v17H7zM11 12h9M11 16h9M11 20h6"/></svg>Our Story</div>
    <div class="nav-item" style="left:637px"><svg viewBox="0 0 30 30"><path d="M4 26h22M7 26V16h4v10M13 26V11h4v15M19 26V7h4v19"/></svg>Investment Strategy</div>
    <div class="nav-item" style="left:812px"><svg viewBox="0 0 30 30"><path d="M15 4v22M9 10l6-6 6 6M9 20h12"/></svg>What Sets Us Apart</div>
    <div class="nav-item" style="left:957px"><svg viewBox="0 0 30 30"><path d="M5 9h20v16H5zM11 9V5h8v4M15 13v8"/></svg>Our Portfolio</div>
    <div class="nav-item" style="left:1057px"><svg viewBox="0 0 30 30"><path d="M4 8h22v15H4zM4 8l11 9 11-9"/></svg>Contact</div>
  </nav>
  <h1>EXPERIENCE – STRATEGY – VISION</h1>
  <p>Velmora Partners is a vertically integrated real estate investment firm with a proven four-decade track record. We acquire, reposition, and operate high-performing assets across multiple sectors — always with a focus on exceptional, risk-adjusted returns.</p>
  <div class="btn" style="left:524px;top:449px;width:152px;height:52px">CONTACT US</div>
  <svg class="play" width="140" height="90" viewBox="0 0 140 90">
    <defs><path id="arc" d="M10 72 A62 62 0 0 1 130 72" fill="none"/></defs>
    <text font-family="Barlow,sans-serif" font-weight="700" font-size="20" fill="#fff" letter-spacing="1"><textPath href="#arc" startOffset="50%" text-anchor="middle">PLAY VIDEO</textPath></text>
    <polygon points="61,50 61,70 79,60" fill="#e3222c"/>
  </svg>
</header>

<svg class="shape" width="1200" height="2520" style="top:0">
  <polygon points="0,682 839,682 0,1553" fill="#c9c9c9" role="img" aria-label="Grey-toned photo of a glass office tower"/>
  <polygon points="1200,1467 1200,2520 285,2520" fill="#ececec"/>
  <polygon points="107,1294 551,1294 551,1739 447,1841 447,1520 107,1878" fill="#8c7a66" role="img" aria-label="Photo of a waiting area with leather chairs by a window"/>
  <polygon points="583,1396 721,1396 583,1540" fill="#e3222c"/>
  <polygon points="479,1865 925,1865 925,2300 820,2413 820,2097 479,2449" fill="#5d6b79" role="img" aria-label="Photo of a rooftop terrace with planters and city buildings"/>
  <polygon points="956,1969 1092,1969 956,2108" fill="#e3222c"/>
</svg>

<div class="founded">FOUNDED</div>
<div class="digit" style="left:120px" role="img" aria-label="Numeral filled with a photo of an office worker">1</div>
<div class="digit" style="left:350px" role="img" aria-label="Numeral filled with a photo of colleagues in a meeting">9</div>
<div class="digit" style="left:607px" role="img" aria-label="Numeral filled with a photo of a woman reviewing documents">8</div>
<div class="digit" style="left:864px" role="img" aria-label="Numeral filled with a photo of a man in a suit">9</div>

<div class="stat-num" style="left:792px;top:1472px">23,000+</div>
<div class="stat-text" style="left:792px;top:1530px">MULTIFAMILY &amp;<br>HEALTHCARE<br>UNITS</div>
<div class="stat-num" style="left:107px;top:2082px">$300+</div>
<div class="stat-text" style="left:107px;top:2141px">MILLION INVESTED<br>IN RENOVATIONS</div>

<footer class="footer">
  <svg class="shape" width="1200" height="901">
    <polygon points="0,0 285,0 0,327" fill="#1d1d1d"/>
    <rect x="285" y="0" width="2" height="327" fill="#1a1a1a"/>
    <polygon points="1200,705 1200,901 1035,901" fill="#2a2a2a"/>
  </svg>
  <div class="foot-brand">VELMORA</div>
  <div class="form-title">CAREER INQUIRIES</div>
  <div class="field" style="top:258px;height:65px"><div class="field-label">NAME</div><div class="field-value">JOHN DOE</div></div>
  <div class="field" style="top:380px;height:39px"><div class="field-label">TYPE YOUR EMAIL...</div></div>
  <div class="field" style="top:491px;height:39px"><div class="field-label">TYPE YOUR MESSAGE...</div></div>
  <div class="btn" style="left:524px;top:573px;width:152px;height:52px">SEND</div>
  <div class="sep"></div>
  <div class="contact-icon" style="left:310px;top:691px">
    <svg width="26" height="36" viewBox="0 0 26 36"><path d="M13 0C6 0 0 6 0 13c0 9 13 23 13 23s13-14 13-23C26 6 20 0 13 0z" fill="#e3222c"/><circle cx="13" cy="13" r="5" fill="#fff"/></svg>
  </div>
  <div class="contact-text" style="left:433px;top:708px"><strong>LOCATE US</strong><br>418 ELM RD. ALDEN,<br>NJ 08000</div>
  <div class="contact-icon" style="left:642px;top:691px">
    <svg width="28" height="20" viewBox="0 0 28 20"><rect width="28" height="20" rx="2" fill="#e3222c"/><path d="M1 2l13 10L27 2" stroke="#fff" stroke-width="2" fill="none"/></svg>
  </div>
  <div class="contact-text" style="left:759px;top:708px"><strong>MAIL US</strong><br>info@velmora.com</div>
  <div class="copy">© 2025 <span>VELMORA</span> ,ALL RIGHT RESERVED</div>
</footer>

</body>
</html>
```